Sci Fi/ Secret Agent Author needs website design!

My name is Talia Brook and I am an author. I require a site that can provide information about myself and my books and other works.

I would like it to have a Home, blog function, (about the) books/series section so people can visit another section and read about each individual book that's going to be released. A resources page, a Store, social media links and ability to load/embed videos from clipvana and other.

I write mild scifi/thriller/conspiracy/secret government type novels. -At the moment-. The series follows a strong female lead that is an agent with a secret organisation in a classified military installation.

The theme would be professional yet possibly show this element.

Target Market(s)

/military fiction/thriller/fantasy/Sci fi/ femme-fatal, readers. Mostly females, age 18-60
Novel readers

Number of Pages Required

5+ page

Requirements
Must have
• Would like designers to follow brief. :)
• My budget includes all the pages I will need;
• eg home, blog, resources, store, ability to pay with coinlark and Credit Cards
• , ability to have trailers from clipvana etc. Must have links to the social media mentioned in the brief.
Nice to have
• use of the colours I have suggested. electric/indigo purple, fuschia highlights , dark greys
• as I will possibly base branding for social media ETC on the look of your website design and colour scheme.
• Ability for trailer on front page??
Should not have
• Should not be too cluttered. (But I am open to all ideas)

```html
<!DOCTYPE html>
<html lang="en">
<head>
<meta charset="utf-8">
<title>Talia Brook – Our Blog</title>
<link href="https://fonts.googleapis.com/css2?family=Open+Sans:ital,wght@0,400;0,600;1,400&family=Roboto+Condensed:wght@400;700&display=swap" rel="stylesheet">
<style>
:root{
  --purple:#6a0aa8;
  --purple-dark:#4a0677;
  --ink:#333333;
  --muted:#666666;
  --rule:#e4e4e4;
  --footer-bg:#f2f2f2;
  --star:#f0a81c;
  --charcoal:#2b2b2b;
  --white:#ffffff;
}
*{margin:0;padding:0;box-sizing:border-box}
html,body{width:1200px;height:2497px;overflow:hidden;background:var(--white)}
body{position:relative;font-family:"Open Sans",Arial,sans-serif;color:var(--ink)}
.abs{position:absolute}

/* header */
.site-header{left:0;top:0;width:1200px;height:97px;background:var(--purple);z-index:3}
.brand{left:97px;top:26px;font:700 40px/1 "Roboto Condensed",Arial,sans-serif;color:var(--white);letter-spacing:.5px}
.main-nav{left:413px;top:42px;display:flex;gap:28px;font:400 14px/1 "Roboto Condensed",Arial,sans-serif;color:var(--white);text-transform:uppercase}
.social-dots{left:1018px;top:44px;display:flex;gap:7px}
.social-dots span{width:11px;height:11px;border-radius:50%;background:var(--white);display:block}

/* hero */
.hero{left:0;top:97px;width:1200px;height:380px;background:radial-gradient(ellipse at 55% 55%,#3c3a48 0%,#23202c 45%,#15121c 100%)}
.hero-title{left:0;top:240px;width:1200px;text-align:center;font:400 37px/1 "Roboto Condensed",Arial,sans-serif;color:var(--white)}
.hero-sub{left:0;top:293px;width:1200px;text-align:center;font:400 14px/27px "Roboto Condensed",Arial,sans-serif;color:var(--white);text-transform:uppercase}
.hero-curve{left:0;top:400px;z-index:2}

/* posts */
.post{left:100px;width:683px;height:269px;border-bottom:1px solid var(--rule)}
.post-media{left:0;top:0;width:306px;height:226px}
.post-title{left:334px;top:-2px;width:340px;font:400 18px/26px "Roboto Condensed",Arial,sans-serif;color:var(--purple)}
.post-meta{left:334px;top:66px;display:flex;gap:38px;font:italic 400 12px/1 "Open Sans",Arial,sans-serif;color:var(--muted)}
.post-meta span{display:flex;align-items:center;gap:8px}
.post-excerpt{left:334px;top:98px;width:350px;font:400 11.5px/21px "Open Sans",Arial,sans-serif;color:var(--muted)}
.read-more{left:334px;top:199px;width:104px;height:27px;border:1px solid var(--purple);color:var(--purple);font:700 12px/25px "Roboto Condensed",Arial,sans-serif;text-align:center}

/* sidebar */
.search{left:837px;top:562px;width:264px;height:42px;border:1px solid #cfcfcf;font:400 11px/40px "Open Sans",Arial,sans-serif;color:#555;padding-left:16px}
.search svg{position:absolute;right:16px;top:14px}
.author-card{left:837px;top:639px;width:264px;height:300px;border:1px solid var(--rule);background:#fafafa}
.author-card .band{position:absolute;left:-1px;top:-1px;width:264px;height:73px;background:var(--purple)}
.avatar{position:absolute;left:74px;top:18px;width:114px;height:114px;border-radius:50%;border:3px solid var(--white);background:radial-gradient(circle at 50% 40%,#9a7a62,#4a3528)}
.author-title{position:absolute;left:0;top:150px;width:262px;text-align:center;font:400 17px/1 "Roboto Condensed",Arial,sans-serif;color:var(--ink)}
.author-text{position:absolute;left:20px;top:178px;width:222px;text-align:center;font:italic 400 10.5px/19px "Open Sans",Arial,sans-serif;color:var(--muted)}
.stars{color:var(--star);font-size:11px;letter-spacing:1px}
.stars .off{color:#c8c8c8}
.author-card .stars{position:absolute;left:0;top:266px;width:262px;text-align:center}

.tabs{left:837px;top:972px;width:264px;height:482px;border:1px solid var(--rule)}
.tab-recent{position:absolute;left:0;top:0;width:132px;height:44px;font:400 19px/46px "Roboto Condensed",Arial,sans-serif;color:var(--purple);text-align:center;text-transform:uppercase}
.tab-popular{position:absolute;left:131px;top:-1px;width:133px;height:45px;background:var(--purple);font:400 19px/44px "Roboto Condensed",Arial,sans-serif;color:var(--white);text-align:center;text-transform:uppercase}
.mini{position:absolute;left:14px;width:234px;height:130px;border-bottom:1px solid var(--rule)}
.mini:last-child{border-bottom:0}
.mini-thumb{position:absolute;left:0;top:0;width:100px;height:107px}
.mini-title{position:absolute;left:116px;top:2px;font:400 13.5px/1 "Open Sans",Arial,sans-serif;color:var(--ink)}
.mini .stars{position:absolute;left:116px;top:24px}
.mini-text{position:absolute;left:116px;top:44px;width:120px;font:400 10.5px/16px "Open Sans",Arial,sans-serif;color:var(--muted)}

.categories-head{left:837px;top:1493px;width:264px;height:40px;background:var(--purple);font:400 19px/40px "Roboto Condensed",Arial,sans-serif;color:var(--white);padding-left:16px;text-transform:uppercase}
.categories{left:837px;top:1558px;list-style:none;font:400 12.5px/31px "Open Sans",Arial,sans-serif;color:var(--ink)}

/* newsletter */
.newsletter{left:0;top:1804px;width:1200px;height:343px;background:linear-gradient(180deg,#7a1fbd 0%,#8e33cf 55%,#7b22b8 100%)}
.news-title{left:0;top:1870px;width:1200px;text-align:center;font:700 30px/1 "Roboto Condensed",Arial,sans-serif;color:var(--white);text-transform:uppercase}
.news-text{left:290px;top:1914px;width:620px;text-align:center;font:600 10.5px/19px "Open Sans",Arial,sans-serif;color:var(--white)}
.field{top:1977px;width:306px;height:40px;background:var(--white);font:400 11px/40px "Open Sans",Arial,sans-serif;color:#555;text-align:center}
.subscribe{left:471px;top:2045px;width:258px;height:42px;background:var(--charcoal);color:var(--white);font:400 16px/42px "Roboto Condensed",Arial,sans-serif;text-align:center;text-transform:uppercase}

/* footer */
.site-footer{left:0;top:2147px;width:1200px;height:287px;background:var(--footer-bg)}
.footer-brand{left:97px;top:2202px;font:700 36px/1 "Roboto Condensed",Arial,sans-serif;color:var(--purple)}
.footer-about{left:97px;top:2255px;width:300px;font:400 11px/21px "Open Sans",Arial,sans-serif;color:var(--muted)}
.footer-head{top:2196px;font:400 18px/1 "Roboto Condensed",Arial,sans-serif;color:var(--ink);text-transform:uppercase}
.contact-row{left:474px;display:flex;gap:14px;font:400 12px/20px "Open Sans",Arial,sans-serif;color:var(--ink)}
.contact-row svg{flex:none;margin-top:3px}
.quick-links{left:790px;top:2234px;list-style:none;font:400 11px/20.5px "Open Sans",Arial,sans-serif;color:var(--ink)}
.quick-links li::before{content:"";display:inline-block;border-left:5px solid var(--ink);border-top:3.5px solid transparent;border-bottom:3.5px solid transparent;margin-right:10px}
.social-list{left:998px;top:2234px;list-style:none;font:400 14px/33.5px "Open Sans",Arial,sans-serif;color:var(--ink)}
.social-list li{display:flex;align-items:center;gap:9px}
.social-list li::before{content:"";width:23px;height:23px;border:1px solid #555;border-radius:50%;display:block}
.bottom-bar{left:0;top:2434px;width:1200px;height:63px;border-top:1px solid var(--rule);font:400 11px/58px "Open Sans",Arial,sans-serif;color:var(--ink);text-align:center}
</style>
</head>
<body>

<header class="abs site-header">
  <div class="abs brand">TALIA BROOK</div>
  <nav class="abs main-nav">
    <span>Home</span><span>Books</span><span>Blog</span><span>Resources</span><span>Other Works</span><span>Store</span><span>Contact Us</span>
  </nav>
  <div class="abs social-dots"><span></span><span></span><span></span><span></span><span></span></div>
</header>

<section class="abs hero" role="img" aria-label="Dark library scene with a hooded figure among bookshelves"></section>
<h1 class="abs hero-title">OUR BLOG</h1>
<p class="abs hero-sub">I am an author and write mild scifi / secret agent /<br>thriller / conspiracy novels</p>
<svg class="abs hero-curve" width="1200" height="80" viewBox="0 0 1200 80" aria-hidden="true">
  <path d="M0,16 C300,52 800,74 1200,50 L1200,80 L0,80 Z" fill="#ffffff"/>
  <path d="M0,16 C300,52 800,74 1200,50" fill="none" stroke="#6a0aa8" stroke-width="5"/>
</svg>

<article class="abs post" style="top:561px">
  <div class="abs post-media" role="img" aria-label="Photo of a long-haired woman in a pale dress facing a misty forest" style="background:linear-gradient(180deg,#8e9a9c,#3d4745)"></div>
  <h2 class="abs post-title">Nemo enim ipsam voluptatem quia voluptas sit aspernatur Sed ut perspiciatis</h2>
  <div class="abs post-meta"><span>▦ Jan 25, 2017</span><span>◯ 2 comments</span></div>
  <p class="abs post-excerpt">Sed ut perspiciatis unde omnis iste natus error sit voluptatem accusantium doloremque laudantium, totam rem aperiam, eaque ipsa quae ab illo inventore veritatis et quasi architecto beatae vitae dicta sunt explicabo. Nemo enim ipsam</p>
  <div class="abs read-more">READ MORE ›</div>
</article>

<article class="abs post" style="top:869px">
  <div class="abs post-media" role="img" aria-label="Photo of a woman with flying dark hair in a green wood" style="background:linear-gradient(160deg,#7f9a5a,#2f3b26)"></div>
  <h2 class="abs post-title">Nemo enim ipsam voluptatem quia voluptas sit aspernatur Sed ut perspiciatis</h2>
  <div class="abs post-meta"><span>▦ Jan 25, 2017</span><span>◯ 2 comments</span></div>
  <p class="abs post-excerpt">Sed ut perspiciatis unde omnis iste natus error sit voluptatem accusantium doloremque laudantium, totam rem aperiam, eaque ipsa quae ab illo inventore veritatis et quasi architecto beatae vitae dicta sunt explicabo. Nemo enim ipsam</p>
  <div class="abs read-more">READ MORE ›</div>
</article>

<article class="abs post" style="top:1169px">
  <div class="abs post-media" role="img" aria-label="Photo of a zombie figure in torn clothing" style="background:linear-gradient(160deg,#7a7470,#3a2e2a)"></div>
  <h2 class="abs post-title">Nemo enim ipsam voluptatem quia voluptas sit aspernatur Sed ut perspiciatis</h2>
  <div class="abs post-meta"><span>▦ Jan 25, 2017</span><span>◯ 2 comments</span></div>
  <p class="abs post-excerpt">Sed ut perspiciatis unde omnis iste natus error sit voluptatem accusantium doloremque laudantium, totam rem aperiam, eaque ipsa quae ab illo inventore veritatis et quasi architecto beatae vitae dicta sunt explicabo. Nemo enim ipsam</p>
  <div class="abs read-more">READ MORE ›</div>
</article>

<article class="abs post" style="top:1477px;border-bottom:0">
  <div class="abs post-media" role="img" aria-label="Photo of a blindfolded figure with a radiant halo in cold blue tones" style="background:linear-gradient(160deg,#9aa3b3,#3b4356)"></div>
  <h2 class="abs post-title">Nemo enim ipsam voluptatem quia voluptas sit aspernatur Sed ut perspiciatis</h2>
  <div class="abs post-meta"><span>▦ Jan 25, 2017</span><span>◯ 2 comments</span></div>
  <p class="abs post-excerpt">Sed ut perspiciatis unde omnis iste natus error sit voluptatem accusantium doloremque laudantium, totam rem aperiam, eaque ipsa quae ab illo inventore veritatis et quasi architecto beatae vitae dicta sunt explicabo. Nemo enim ipsam</p>
  <div class="abs read-more">READ MORE ›</div>
</article>

<div class="abs search">SEARCH
  <svg width="13" height="13" viewBox="0 0 13 13" aria-hidden="true"><circle cx="5.5" cy="5.5" r="4" fill="none" stroke="#555" stroke-width="1.8"/><line x1="8.5" y1="8.5" x2="12" y2="12" stroke="#555" stroke-width="1.8"/></svg>
</div>

<aside class="abs author-card">
  <div class="band"></div>
  <div class="avatar" role="img" aria-label="Author portrait"></div>
  <h3 class="author-title">I AM AN AUTHOR</h3>
  <p class="author-text">Lorem ipsum dolor sit amet, consectetur adipiscing elit, sed do eiusmod tempor incididunt ut labore et dolore magna aliqua. Ut enim ad minim veniam, quis nostrud Lorem</p>
  <div class="stars">★★★<span class="off">★★</span></div>
</aside>

<aside class="abs tabs">
  <div class="tab-recent">Recent</div>
  <div class="tab-popular">Popular</div>
  <div class="mini" style="top:67px">
    <div class="mini-thumb" role="img" aria-label="Grey photo of a dark-haired ghostly figure" style="background:linear-gradient(180deg,#b8b8b8,#3a3a3a)"></div>
    <div class="mini-title">Nemo enim ipsam</div>
    <div class="stars">★★★<span class="off">★★</span></div>
    <p class="mini-text">Lorem ipsum dolor sit ctetur adipiscing elit, sed do eiusmod tempor</p>
  </div>
  <div class="mini" style="top:212px">
    <div class="mini-thumb" role="img" aria-label="Grey photo of a lone figure in a foggy forest" style="background:linear-gradient(180deg,#c4c4c4,#5a5a5a)"></div>
    <div class="mini-title">Nemo enim ipsam</div>
    <div class="stars">★★★<span class="off">★★</span></div>
    <p class="mini-text">Lorem ipsum dolor sit ctetur adipiscing elit, sed do eiusmod tempor</p>
  </div>
  <div class="mini" style="top:357px">
    <div class="mini-thumb" role="img" aria-label="Photo of an old doll lying on stones" style="background:linear-gradient(160deg,#8c8a88,#4c4846)"></div>
    <div class="mini-title">Nemo enim ipsam</div>
    <div class="stars">★★★<span class="off">★★</span></div>
    <p class="mini-text">Lorem ipsum dolor sit ctetur adipiscing elit, sed do eiusmod tempor</p>
  </div>
</aside>

<h3 class="abs categories-head">Categories</h3>
<ul class="abs categories">
  <li>Sed ut perspiciatis unde omnis</li>
  <li>Excepteur sint occaecat</li>
  <li>Ut enim ad minima veniam</li>
  <li>Neque porro quisquam</li>
  <li>Quis autem vel eum iure</li>
</ul>

<section class="abs newsletter" role="img" aria-label="Purple-toned photo of a desert road stretching to mountains"></section>
<h2 class="abs news-title">Sign up for our newsletter</h2>
<p class="abs news-text">Sed ut perspiciatis unde omnis iste natus error sit voluptatem accusantium doloremque laudantium, totam rem aperiam, eaque ipsa quae ab illo inventore veritatis et quasi architecto beatae vitae dicta sunt explicabo</p>
<div class="abs field" style="left:288px">Enter Name</div>
<div class="abs field" style="left:606px">Enter Email</div>
<div class="abs subscribe">Subscribe</div>

<footer class="abs site-footer"></footer>
<div class="abs footer-brand">TALIA BROOK</div>
<p class="abs footer-about">Sed ut perspiciatis unde omnis iste natus error sit voluptatem accusantium doloremque lauantium, totam rem aperiam, eaque ipsa quae ab illo inventore veritatis et quasi architecto beatae vitae dicta sunt explicabo</p>

<h4 class="abs footer-head" style="left:474px">Contact Us</h4>
<div class="abs contact-row" style="top:2236px">
  <svg width="12" height="16" viewBox="0 0 12 16" aria-hidden="true"><path d="M6,0 C2.7,0 0,2.6 0,5.8 C0,10 6,16 6,16 C6,16 12,10 12,5.8 C12,2.6 9.3,0 6,0 Z" fill="#444"/><circle cx="6" cy="5.8" r="2.2" fill="#f2f2f2"/></svg>
  <div>Talia Brook<br>Lindenpfad 12 40210 Hallbrook</div>
</div>
<div class="abs contact-row" style="top:2292px">
  <svg width="13" height="13" viewBox="0 0 13 13" aria-hidden="true"><path d="M2.5,0.5 L5,3.5 L3.6,5.2 C4.5,7 6,8.5 7.8,9.4 L9.5,8 L12.5,10.5 L11,12.5 C5.5,12.5 0.5,7.5 0.5,2 Z" fill="#444"/></svg>
  <div>Phone: +49 555 01 24 870</div>
</div>
<div class="abs contact-row" style="top:2322px">
  <svg width="13" height="10" viewBox="0 0 13 10" aria-hidden="true"><rect x="0" y="0" width="13" height="10" fill="#444"/><path d="M0.5,0.8 L6.5,5.5 L12.5,0.8" fill="none" stroke="#f2f2f2" stroke-width="1.2"/></svg>
  <div>info@taliabrook.com</div>
</div>

<h4 class="abs footer-head" style="left:787px">Quick Links</h4>
<ul class="abs quick-links">
  <li>Home</li><li>About the book</li><li>Blog</li><li>Resources</li><li>Blog</li><li>store</li><li>Contact Us</li>
</ul>

<h4 class="abs footer-head" style="left:998px">Social</h4>
<ul class="abs social-list">
  <li>Linkwall</li><li>Chirply</li><li>Picturely</li><li>Pinboardly</li><li>clipvana</li>
</ul>

<div class="abs bottom-bar">©2017 Talia Brook, All Rights Reserved.</div>

</body>
</html>
```